Card and letterhead for a financial planning firm
Bright Harbor Associates
Professional
Neil Vardakian
Senior Account Executive
4780 W. Meadow Rd
State College, PA 16934
neil@brightharborpa.example
www.brightharborpa.example
I prefer to have a larger font, I don't like cards that make you squint to read the info.
the logo
Please use this logo. Don't be afraid to change the layout of the logo if it enhances the design as in placing the logo next to the name vs. over it.

```html
<!DOCTYPE html>
<html lang="en">
<head>
<meta charset="utf-8">
<title>Bright Harbor Associates – Business Card</title>
<link href="https://fonts.googleapis.com/css2?family=Montserrat:wght@700&family=Open+Sans:wght@400;600&display=swap" rel="stylesheet">
<style>
  :root {
    --backdrop: #2a2b2e;
    --card: #ffffff;
    --brand-blue: #1f5aa8;
    --deep-blue: #1c3f8f;
    --lime: #9cc63b;
    --text-grey: #5b5f66;
    --rule-grey: #c9ccd1;
    --photo-light: #d9dde3;
    --photo-dark: #4a5260;
  }
  * { margin: 0; padding: 0; box-sizing: border-box; }
  html, body { width: 1200px; height: 871px; overflow: hidden; }
  body {
    background: var(--backdrop);
    font-family: "Open Sans", Arial, sans-serif;
    color: var(--text-grey);
  }
  .card {
    position: absolute;
    left: 75px; top: 135px;
    width: 1050px; height: 600px;
    background: var(--card);
    overflow: hidden;
  }
  .card-art { position: absolute; inset: 0; }
  .brand {
    position: absolute;
    left: 70px; top: 70px;
    display: flex; align-items: center; gap: 14px;
  }
  .brand-dot {
    width: 46px; height: 46px; border-radius: 50%;
    background: var(--brand-blue);
  }
  .brand-name {
    font-family: "Montserrat", Arial, sans-serif;
    font-weight: 700;
    font-size: 26px;
    letter-spacing: 0.5px;
    color: var(--brand-blue);
    text-transform: uppercase;
    line-height: 1.15;
  }
  .accent-tab {
    position: absolute;
    left: 0; top: 196px;
    width: 34px; height: 40px;
    background: var(--lime);
  }
  .person { position: absolute; left: 56px; top: 196px; }
  .person-name {
    font-size: 28px; font-weight: 600;
    color: var(--brand-blue);
    line-height: 1.1;
  }
  .person-title { font-size: 17px; margin-top: 4px; }
  .address {
    position: absolute; left: 56px; top: 290px;
    font-size: 17px; line-height: 1.4;
  }
  .contacts {
    position: absolute; left: 56px; top: 375px;
    display: flex;
    font-size: 17px; line-height: 1.45;
  }
  .contacts-phone { padding-right: 28px; }
  .contacts-other {
    padding-left: 22px;
    border-left: 2px solid var(--rule-grey);
  }
  .website {
    position: absolute; left: 56px; top: 500px;
    font-size: 17px; font-weight: 600;
    color: var(--text-grey);
  }
</style>
</head>
<body>
  <main class="card">
    <svg class="card-art" width="1050" height="600" viewBox="0 0 1050 600" aria-hidden="false">
      <defs>
        <linearGradient id="portraitTone" x1="0" y1="0" x2="0" y2="1">
          <stop offset="0" stop-color="var(--photo-light)"/>
          <stop offset="1" stop-color="var(--photo-dark)"/>
        </linearGradient>
      </defs>
      <path role="img" aria-label="Portrait photo of the account executive"
            d="M 880 0 C 640 110, 600 470, 800 600 L 1050 600 L 1050 0 Z"
            fill="url(#portraitTone)"/>
      <path d="M 880 0 C 640 110, 600 470, 800 600" fill="none" stroke="var(--deep-blue)" stroke-width="18"/>
      <path d="M 1050 30 C 930 40, 790 110, 720 200" fill="none" stroke="var(--lime)" stroke-width="7" stroke-linecap="round"/>
    </svg>

    <div class="brand">
      <span class="brand-dot"></span>
      <span class="brand-name">Bright Harbor<br>Associates</span>
    </div>

    <span class="accent-tab"></span>
    <div class="person">
      <p class="person-name">Neil Vardakian</p>
      <p class="person-title">Senior Account Executive</p>
    </div>

    <address class="address" style="font-style:normal">
      4780 W. Meadow Rd<br>
      State College, PA 16934
    </address>

    <div class="contacts">
      <div class="contacts-phone">
        T: 1.800.555.0142<br>
        P: 814.555.0187<br>
        C: 814.555.0163
      </div>
      <div class="contacts-other">
        F: 814.555.0129<br>
        E: neil@brightharborpa.example
      </div>
    </div>

    <p class="website">www.brightharborpa.example</p>
  </main>
</body>
</html>
```